Thornvale Secure Business Cards

Need high quality business card designed around my company logo. Ideally the cards need to be a glossy black as the logo goes well with a black background.

The company is a Locksmithing business.

Domestic clients are Residential Home Owners and Landlords. Commercial clients are local businesses, estate agents, landlords, solicitors

Services offered :
Emergency Lock Out
New Lock Fitting & Replacement
High Security Upgrades
UPVC lock repairs
Mobile Key Cutting
Free Security Reviews

Qualificatons & Certifications:
Accredited Fenwick & Marrow NVQ Level 3, TQBA
Fully Insured
PVR Checked

Contact & Business Details:

Business Name : Thornvale Secure
Name: Rob Kessington
Tel: 01632 960481 Office / 07700900417 Mobile
Email: contact@thornvalesecure-demo.com
Website: www.thornvalesecure-demo.com

(please note that the website is currently under development and not available to view)

Industry/Entity Type

Locksmith

Contact Information for Business Card

Name: Rob Kessington

Services:
Emergency Lock Out
High Security Upgrades
UPVC lock repairs
Mobile Key Cutting
Free Security Reviews

Requirements
Must have
• Ideally the cards should be a glossy black as the logo stands out better on a black background.

Logo on front and the word LOCKSMITH should be incorporated into the front design of the card.

Qualifications & Certifications on the back ideally along the top / bottom of the card or split (I.e along the top “ Accredited : Fenwick & Marrow Level 3 , TQBA”
and along the bottom , “Fully Insured & PVR Checked”

Services offered ideally listed on the back of the card, preferably split into two columns. If possible the logo could also be incorporated onto the back of the card between the two services columns (I.e the services listed either side of the logo)
Nice to have
• On the back of the card, have the logo in the middle with the services listed either side of the logo I.e 3 services on left of logo and three to the right.

```html
<!DOCTYPE html>
<html lang="en">
<head>
<meta charset="utf-8">
<title>Thornvale Secure – Business Cards</title>
<link rel="stylesheet" href="https://fonts.googleapis.com/css2?family=Krona+One&family=Questrial&display=swap">
<style>
  :root {
    --page: #ffffff;
    --card: #000000;
    --gold: #c28b2c;
    --gold-light: #e3b54a;
    --white: #ffffff;
    --icon-fill: #1c1c1c;
    --display: "Krona One", sans-serif;
    --body: "Questrial", sans-serif;
  }
  * { margin: 0; padding: 0; box-sizing: border-box; }
  html, body { width: 1200px; height: 1200px; overflow: hidden; background: var(--page); }
  .canvas { position: relative; width: 1200px; height: 1200px; }
  .card { position: absolute; left: 216px; width: 775px; height: 430px; background: var(--card); overflow: hidden; }
  .card--front { top: 153px; }
  .card--back { top: 624px; }

  .brand-mark { position: absolute; width: 194px; height: 194px; }
  .brand-mark svg { position: absolute; inset: 0; }
  .brand-mark__name {
    position: absolute; inset: 0; display: flex; align-items: center; justify-content: center;
    text-align: center; font-family: var(--body); color: var(--gold-light);
    font-size: 25px; line-height: 1.15; letter-spacing: 1px; text-transform: uppercase;
  }
  .card--front .brand-mark { left: 96px; top: 100px; }
  .card--back .brand-mark { left: 290px; top: 142px; }

  .trade-title {
    position: absolute; left: 0; width: 386px; top: 323px; text-align: center;
    font-family: var(--display); color: var(--gold); font-size: 31px; letter-spacing: 1px;
  }
  .divider {
    position: absolute; left: 381px; top: 46px; width: 2px; height: 348px;
    background: linear-gradient(to bottom, #d8d8d8, #9a9a9a 60%, #2a2a2a);
  }
  .person { position: absolute; left: 414px; top: 70px; }
  .person__name { font-family: var(--display); color: var(--white); font-size: 23px; letter-spacing: 0.5px; }
  .person__role { margin-top: 6px; font-family: var(--display); color: var(--white); font-size: 12px; letter-spacing: 1.5px; }
  .person__rule {
    position: absolute; left: 414px; top: 130px; width: 255px; height: 2px;
    background: linear-gradient(to right, #ffffff, #ffffff 60%, #3a3a3a);
  }
  .contacts { position: absolute; left: 414px; top: 168px; list-style: none; }
  .contacts li { display: flex; align-items: center; height: 42px; margin-bottom: 9.5px; }
  .contacts .icon {
    width: 42px; height: 42px; border: 2px solid var(--gold); border-radius: 7px;
    background: var(--icon-fill); display: flex; align-items: center; justify-content: center; flex: none;
  }
  .contacts span { margin-left: 18px; font-family: var(--body); color: var(--white); font-size: 19.5px; }

  .gold-rule { position: absolute; height: 2px; background: var(--gold); }
  .white-rule { position: absolute; height: 2px; background: var(--white); }
  .credential {
    position: absolute; left: 0; width: 775px; text-align: center;
    font-family: var(--display); color: var(--gold); font-size: 17px; letter-spacing: 0.5px;
  }
  .credential--top { top: 35px; }
  .credential--bottom { top: 372px; }
  .services-heading {
    position: absolute; left: 282px; width: 211px; top: 90px; text-align: center;
    font-family: var(--body); font-weight: 700; color: var(--white); font-size: 16px; letter-spacing: 0.5px;
    -webkit-text-stroke: 0.4px var(--white);
  }
  .services { position: absolute; list-style: none; font-family: var(--body); color: var(--white); font-size: 19.5px; line-height: 26px; }
  .services li { position: relative; padding-left: 26px; }
  .services li::before { content: ""; position: absolute; left: 0; top: 13px; width: 10px; height: 3px; background: var(--white); }
  .services--left { left: 30px; top: 174px; width: 240px; }
  .services--left li:nth-child(2) { margin-top: 10px; }
  .services--left li:nth-child(3) { margin-top: 6px; }
  .services--right { left: 506px; top: 174px; width: 260px; }
  .services--right li + li { margin-top: 21px; }
</style>
</head>
<body>
<main class="canvas">

  <section class="card card--front">
    <div class="brand-mark">
      <svg viewBox="0 0 194 194" aria-hidden="true"><circle cx="97" cy="97" r="94" fill="none" stroke="#c28b2c" stroke-width="3"/></svg>
      <div class="brand-mark__name">Thornvale<br>Secure</div>
    </div>
    <div class="trade-title">LOCKSMITH</div>

    <div class="divider"></div>

    <div class="person">
      <div class="person__name">ROB KESSINGTON</div>
      <div class="person__role">CEO/OWNER</div>
    </div>
    <div class="person__rule"></div>

    <ul class="contacts">
      <li>
        <div class="icon"><svg width="22" height="22" viewBox="0 0 24 24"><path d="M6.6 2.5l3 3.3-1.8 2.6c1.2 2.8 3.2 4.8 5.9 6l2.6-1.8 3.3 3-1.8 3.2c-7.8-.6-13.7-6.6-14.4-14.4z" fill="#c28b2c"/></svg></div>
        <span>016 - 3296 - 0481</span>
      </li>
      <li>
        <div class="icon"><svg width="22" height="22" viewBox="0 0 24 24"><path d="M3 8c0-2 4-3.5 9-3.5s9 1.5 9 3.5v1.5h-4V8H7v1.5H3z" fill="#c28b2c"/><rect x="5" y="10" width="14" height="10" rx="1.5" fill="#c28b2c"/><circle cx="12" cy="15" r="3" fill="#1c1c1c"/></svg></div>
        <span>077 - 0090 - 0417</span>
      </li>
      <li>
        <div class="icon"><svg width="24" height="24" viewBox="0 0 24 24"><rect x="3" y="5.5" width="18" height="13" fill="#c28b2c"/><path d="M3 5.5l9 7 9-7M3 18.5l7-6M21 18.5l-7-6" fill="none" stroke="#1c1c1c" stroke-width="1.3"/></svg></div>
        <span>contact@thornvalesecure-demo.com</span>
      </li>
      <li>
        <div class="icon"><svg width="24" height="24" viewBox="0 0 24 24" fill="none" stroke="#c28b2c" stroke-width="1.4"><circle cx="12" cy="12" r="9"/><ellipse cx="12" cy="12" rx="4" ry="9"/><path d="M3 12h18M4.5 7.5h15M4.5 16.5h15M12 3v18"/></svg></div>
        <span>www.thornvalesecure-demo.com</span>
      </li>
    </ul>
  </section>

  <section class="card card--back">
    <div class="gold-rule" style="left:46px;top:48px;width:38px"></div>
    <div class="credential credential--top">Accredited Fenwick &amp; Marrow NVQ Level 3, TQBA</div>
    <div class="gold-rule" style="left:691px;top:48px;width:38px"></div>

    <div class="white-rule" style="left:19px;top:98px;width:263px"></div>
    <div class="services-heading">OUR SERVICES</div>
    <div class="white-rule" style="left:493px;top:98px;width:263px"></div>

    <ul class="services services--left">
      <li>Emergency Lock Out</li>
      <li>New Lock Fitting &amp; Replacement</li>
      <li>High Security Upgrades</li>
    </ul>

    <div class="brand-mark">
      <svg viewBox="0 0 194 194" aria-hidden="true"><circle cx="97" cy="97" r="94" fill="none" stroke="#c28b2c" stroke-width="3"/></svg>
      <div class="brand-mark__name">Thornvale<br>Secure</div>
    </div>

    <ul class="services services--right">
      <li>UPVC lock repairs</li>
      <li>Mobile Key Cutting</li>
      <li>Free Security Reviews</li>
    </ul>

    <div class="gold-rule" style="left:46px;top:384px;width:130px"></div>
    <div class="credential credential--bottom">Fully Insured &amp; PVR Checked</div>
    <div class="gold-rule" style="left:598px;top:384px;width:130px"></div>
  </section>

</main>
</body>
</html>
```